" CLÍNICA FUNCIONA HÁ 16 ANOS, COM ATENDIMENTOS PARTICULARES, VOLTADOS PRIMORDIALMENTE A PROCEDIMENTOS ESTÉTICOS DE ALTO PADRÃO, INCLUINDO DERVIX, PREENCHIMENTOS, LASERS ... "

```html
<!DOCTYPE html>
<html lang="pt-BR">
<head>
<meta charset="UTF-8">
<title>Velura Clínica — Cartão de Visita</title>
<link rel="stylesheet" href="https://fonts.googleapis.com/css2?family=Cinzel:wght@400;600&family=Montserrat:ital,wght@0,400;0,500;0,700;1,400&display=swap">
<style>
  :root{
    --bg:#ecebe8;
    --card:#ffffff;
    --ink:#2e2a27;
    --muted:#555049;
    --gold-dark:#b8892c;
    --gold:#d9b45a;
    --gold-light:#f3dc95;
    --rule:#c9c9c9;
    --icon:#333333;
  }
  *{margin:0;padding:0;box-sizing:border-box}
  html,body{width:1200px;height:1200px;overflow:hidden;background:var(--bg)}
  .sheet{position:relative;width:1200px;height:1200px}
  .card{
    position:absolute;left:240px;width:720px;height:410px;
    background:var(--card);border-radius:18px;overflow:hidden;
    box-shadow:0 10px 30px rgba(0,0,0,.12);
  }
  .card--front{top:150px}
  .card--back{top:650px}
  .gold-band{
    position:absolute;left:0;right:0;bottom:0;height:30px;
    background:linear-gradient(90deg,var(--gold-dark),var(--gold-light) 35%,var(--gold) 60%,var(--gold-light) 80%,var(--gold-dark));
  }
  .brand{
    position:absolute;left:0;right:0;top:60px;
    display:flex;flex-direction:column;align-items:center;
  }
  .brand__mark{width:110px;height:110px}
  .brand__name{
    font-family:"Cinzel",serif;font-weight:400;font-size:58px;
    letter-spacing:3px;color:var(--ink);margin-top:10px;line-height:1;
  }
  .brand__sub{
    display:flex;align-items:center;gap:12px;margin-top:10px;
    font-family:"Montserrat",sans-serif;font-size:15px;letter-spacing:8px;
    color:var(--gold-dark);
  }
  .brand__sub::before,.brand__sub::after{
    content:"";display:block;width:70px;height:1px;background:var(--gold);
  }
  .decor-circle{position:absolute;left:-20px;top:-30px;width:340px;height:340px}
  .contact{
    position:absolute;right:34px;top:70px;width:330px;
    font-family:"Montserrat",sans-serif;color:var(--muted);text-align:right;
  }
  .contact__name{font-weight:700;font-size:17px;letter-spacing:4px;color:var(--ink)}
  .contact__role{font-style:italic;font-size:12px;margin-top:4px;margin-right:14px}
  .contact__rule{height:1px;background:var(--rule);margin:10px 0 18px}
  .contact__list{list-style:none}
  .contact__item{
    display:flex;justify-content:flex-end;align-items:flex-start;gap:16px;
    font-size:13px;line-height:1.45;margin-bottom:12px;
  }
  .contact__icon{flex:none;width:16px;height:16px;margin-top:1px}
</style>
</head>
<body>
<main class="sheet">

  <section class="card card--front" aria-label="Frente do cartão">
    <div class="brand">
      <svg class="brand__mark" viewBox="0 0 110 110" aria-hidden="true">
        <defs>
          <linearGradient id="goldStroke" x1="0" y1="0" x2="1" y2="1">
            <stop offset="0" stop-color="#b8892c"/>
            <stop offset=".5" stop-color="#f3dc95"/>
            <stop offset="1" stop-color="#b8892c"/>
          </linearGradient>
        </defs>
        <circle cx="55" cy="55" r="50" fill="none" stroke="url(#goldStroke)" stroke-width="3"/>
      </svg>
      <div class="brand__name">VELURA</div>
      <div class="brand__sub">CLÍNICA</div>
    </div>
    <div class="gold-band"></div>
  </section>

  <section class="card card--back" aria-label="Verso do cartão">
    <svg class="decor-circle" viewBox="0 0 340 340" aria-hidden="true">
      <defs>
        <linearGradient id="goldStrokeBig" x1="0" y1="0" x2="1" y2="1">
          <stop offset="0" stop-color="#b8892c"/>
          <stop offset=".5" stop-color="#f3dc95"/>
          <stop offset="1" stop-color="#b8892c"/>
        </linearGradient>
      </defs>
      <circle cx="170" cy="170" r="155" fill="none" stroke="url(#goldStrokeBig)" stroke-width="6"/>
    </svg>

    <div class="contact">
      <div class="contact__name">NOME SOBRENOME</div>
      <div class="contact__role">cargo</div>
      <div class="contact__rule"></div>
      <ul class="contact__list">
        <li class="contact__item">XX XXXX-XXXX
          <svg class="contact__icon" viewBox="0 0 16 16" aria-hidden="true"><rect width="16" height="16" rx="3" fill="var(--icon)"/><rect x="5" y="3" width="6" height="10" rx="1" fill="none" stroke="#fff" stroke-width="1.2"/></svg>
        </li>
        <li class="contact__item">XX XXXX-XXXX
          <svg class="contact__icon" viewBox="0 0 16 16" aria-hidden="true"><rect width="16" height="16" rx="3" fill="var(--icon)"/><path d="M4.5 4c1 3 3 6 7 7.5l.8-1.6-2-1-1 .8C8 9 7 8 6.3 6.8l.8-1-1-2z" fill="#fff"/></svg>
        </li>
        <li class="contact__item">contato@xxxx.com.br
          <svg class="contact__icon" viewBox="0 0 16 16" aria-hidden="true"><rect width="16" height="16" rx="3" fill="var(--icon)"/><rect x="3.5" y="5" width="9" height="6.5" fill="none" stroke="#fff" stroke-width="1.1"/><path d="M3.5 5l4.5 3.5L12.5 5" fill="none" stroke="#fff" stroke-width="1.1"/></svg>
        </li>
        <li class="contact__item">www.xxxx.com.br
          <svg class="contact__icon" viewBox="0 0 16 16" aria-hidden="true"><rect width="16" height="16" rx="3" fill="var(--icon)"/><circle cx="8" cy="8" r="4.5" fill="none" stroke="#fff" stroke-width="1.1"/><path d="M3.5 8h9M8 3.5c-2 2.5-2 6.5 0 9M8 3.5c2 2.5 2 6.5 0 9" fill="none" stroke="#fff" stroke-width=".9"/></svg>
        </li>
        <li class="contact__item">Nome da rua, número, bairro,<br>Cidade, Estado, CEP
          <svg class="contact__icon" viewBox="0 0 16 16" aria-hidden="true"><rect width="16" height="16" rx="3" fill="var(--icon)"/><path d="M8 13s-3.5-3.6-3.5-6a3.5 3.5 0 0 1 7 0C11.5 9.4 8 13 8 13z" fill="#fff"/><circle cx="8" cy="7" r="1.3" fill="var(--icon)"/></svg>
        </li>
      </ul>
    </div>
    <div class="gold-band"></div>
  </section>

</main>
</body>
</html>
```